Spanish Student Needs a Cover for his PhD Dissertation

Hi everyone :) So, I'm a Corneal surgeon currently finishing my PhD, with a dissertation focused on the evaluation of quality of life in patients affected by a disease called Keratoconus. Just so you know, Keratoconus is a condition in which the cornea (the frontal part of the way) gets thin and bulgy and it decreases vision. What I did during my PhD was designing a questionnaire for evaluating quality of life in this kind of patients.
I need to design a hard cover for my dissertation, which is 200 sheets long. I like kind of minimalistic and geometric designs but I am totally open to suggestions. What needs to be in the cover is the name of the dissertation "Diseño, desarrollo y validación de una encuesta para evaluar el compromiso visual y emocional subjetivos en pacientes con Queratocono" and my name, "Iñigo Tarrasco". The other thing that needs to go there is the logo of my university (Universidad de Montebrisa). Aside from that, anything else is up to the designer. It would be important to use the kind of "red" color I am using in the dissertation. I am attaching the frontal page of my dissertation so you know what kind of design and colors I am using.
In the back part, of the cover, there should be this small inscription: "Iñigo Tarrasco, MD, es un Oftalmólogo Subespecialista en Cirugía Refractiva de la Universidad Serrana Metropolitana (Colombia) y la Universidad de Montebrisa (España). Actualmente se desempeña como miembro del Departamento de Córnea y Cirugía Refractiva de la Clínica de Oftalmología Vallealto y como director de su propia compañía de emprendimiento médico Silver Heron Surgical". Please leave a space to place my picture; I will have it taken this week so I don't have it right now, you can just leave the blank spot and I will include it later
The size of the pages is standard "letter" size.
Thanks a lot!

Target Market(s)

PhD Scholars

Font styles to use
Serif

Requirements
Must have
• The "red" color I use on my font. It must be formal but "young".
Nice to have
• I like to keep the design clean, kind of "formal with a young" touch so to speak. I really like gray colors, so it would be nice to have broad areas of gray. I love geometrical designs.
I have uploaded a very early version a friend of mine made (it even had a different title); this can be a starting point for you to work on, but I am more than open to suggestions and new ideas.
Should not have
• Please don't use my whole name, Iñigo Tarrasco is fine. I don't like ALL CAPITALS.

```html
<!DOCTYPE html>
<html lang="es">
<head>
<meta charset="utf-8">
<title>Cubierta de tesis doctoral – Iñigo Tarrasco</title>
<link rel="stylesheet" href="https://fonts.googleapis.com/css2?family=Noto+Serif:wght@400;700&family=Open+Sans:wght@400;600&display=swap">
<style>
  :root {
    --thesis-red: #a51c3d;
    --paper: #f3f3f3;
    --page-bg: #ffffff;
    --ink: #1d1d1d;
    --eye-dark: #3f4750;
    --eye-mid: #9aa3ad;
  }
  html, body {
    margin: 0;
    width: 1200px;
    height: 1200px;
    overflow: hidden;
    background: var(--page-bg);
  }
  .cover-spread {
    position: absolute;
    left: 30px;
    top: 241px;
    width: 1140px;
    height: 718px;
    background: var(--paper);
  }
  .spine-name {
    position: absolute;
    left: 561px;
    top: 90px;
    writing-mode: vertical-rl;
    font-family: "Noto Serif", serif;
    font-size: 12px;
    color: var(--thesis-red);
    margin: 0;
  }
  .photo-slot {
    position: absolute;
    left: 200px;
    top: 259px;
    width: 146px;
    height: 146px;
    border: 4.5px solid var(--thesis-red);
  }
  .author-bio {
    position: absolute;
    left: 105px;
    top: 455px;
    width: 340px;
    margin: 0;
    font-family: "Open Sans", sans-serif;
    font-size: 12.2px;
    line-height: 14.5px;
    color: var(--ink);
    text-align: justify;
    text-align-last: center;
  }
  .author-bio strong {
    color: var(--thesis-red);
    font-weight: 600;
  }
  .university-mark {
    position: absolute;
    left: 606px;
    top: 38px;
    width: 150px;
    text-align: center;
    font-family: "Noto Serif", serif;
    font-weight: 700;
    font-size: 10px;
    color: var(--thesis-red);
  }
  .university-mark .seal {
    display: block;
    width: 44px;
    height: 44px;
    margin: 0 auto 5px;
    border-radius: 50%;
    border: 1.5px solid var(--thesis-red);
    box-sizing: border-box;
  }
  .doctoral-school {
    position: absolute;
    left: 940px;
    top: 62px;
    width: 170px;
    font-family: "Noto Serif", serif;
    color: var(--thesis-red);
    text-align: right;
  }
  .doctoral-school .acronym {
    display: block;
    font-size: 22px;
    font-weight: 700;
    line-height: 24px;
  }
  .doctoral-school .full-name {
    display: block;
    font-size: 6.5px;
    font-weight: 700;
  }
  .thesis-title {
    position: absolute;
    left: 645px;
    top: 148px;
    width: 416px;
    margin: 0;
    font-family: "Noto Serif", serif;
    font-weight: 400;
    font-size: 26.5px;
    line-height: 27px;
    color: var(--thesis-red);
    text-align: justify;
    text-align-last: center;
  }
  .thesis-title .keyword {
    display: block;
    font-weight: 700;
    text-align: center;
  }
  .eye-artwork {
    position: absolute;
    left: 667px;
    top: 336px;
    width: 383px;
    height: 238px;
  }
  .author-name {
    position: absolute;
    left: 657px;
    top: 652px;
    width: 400px;
    margin: 0;
    text-align: center;
    font-family: "Noto Serif", serif;
    font-size: 27px;
    color: var(--thesis-red);
  }
</style>
</head>
<body>
  <div class="cover-spread">
    <!-- back cover -->
    <div class="photo-slot"></div>
    <p class="author-bio"><strong>Iñigo Tarrasco</strong>, MD, es un Oftalmólogo Subespecialista en Cirugía Refractiva de la Universidad Serrana Metropolitana (Colombia) y la Universidad de Montebrisa (España). Actualmente se desempeña como miembro del Departamento de Córnea y Cirugía Refractiva de la Clínica de Oftalmología Vallealto y como director de su propia compañía de emprendimiento médico Silver Heron Surgical.</p>

    <!-- spine -->
    <p class="spine-name">Iñigo Tarrasco</p>

    <!-- front cover -->
    <div class="university-mark"><span class="seal"></span>Universidad de Montebrisa</div>
    <div class="doctoral-school">
      <span class="acronym">EDUMB</span>
      <span class="full-name">Escuela de Doctorado Universidad de Montebrisa</span>
    </div>

    <h1 class="thesis-title">Diseño, desarrollo y validación de una encuesta para evaluar el compromiso visual y emocional subjetivos en pacientes con <span class="keyword">Queratocono</span></h1>

    <svg class="eye-artwork" role="img" aria-label="Ilustración de un ojo humano en tonos grises con anillos tecnológicos alrededor del iris" viewBox="0 0 383 238">
      <defs>
        <radialGradient id="eye-tone" cx="0.5" cy="0.5" r="0.5">
          <stop offset="0" stop-color="var(--eye-dark)"/>
          <stop offset="0.35" stop-color="var(--eye-mid)" stop-opacity="0.8"/>
          <stop offset="1" stop-color="var(--paper)" stop-opacity="0"/>
        </radialGradient>
      </defs>
      <ellipse cx="200" cy="115" rx="190" ry="118" fill="url(#eye-tone)"/>
    </svg>

    <p class="author-name">Iñigo Tarrasco</p>
  </div>
</body>
</html>
```